varnity.com car care product labeling with cut outs will be printed on holographic sheet.

Need to make label for eco-friendly car care products. no hazard signs.
clean and simple design minimalism
wheel cleaner
tire shiner
glass cleaner
all purpose cleaner
247x90mm
166x150mm

Target Market(s)

eco friendly car care products. europe , uae

Industry/Entity Type

car care products, eco-friendly product line

Requirements
Must have
• BW design print on holographic sheet/label .eco-friendly signs
Nice to have
• premium product look and simplicity will be at first place, can be with cut outs

```html
<!DOCTYPE html>
<html lang="en">
<head>
<meta charset="utf-8">
<title>varnity car care labels</title>
<link rel="stylesheet" href="https://fonts.googleapis.com/css2?family=Oswald:wght@600;700&family=Montserrat:wght@600&display=swap">
<style>
  :root {
    --page: #ffffff;
    --ink: #111111;
    --silver-light: #f2f2f2;
    --silver-mid: #c9c9c9;
    --silver-dark: #a9a9a9;
    --blue-a: #3a9ad8; --blue-b: #1a6fb8; --blue-c: #1c3f68; --blue-brand: #1877c4;
    --pink-a: #e8188a; --pink-b: #d60577; --pink-c: #6e1848; --pink-brand: #e0107f;
    --lime-a: #e4e404; --lime-b: #b8cc12; --lime-c: #3e6a22; --lime-brand: #8cc63f;
    --orange-a: #f28a2a; --orange-b: #e45a1c; --orange-c: #7a2a18; --orange-brand: #e8561f;
  }
  * { box-sizing: border-box; margin: 0; padding: 0; }
  html, body { width: 1200px; height: 849px; overflow: hidden; background: var(--page); }
  .sheet { position: relative; width: 1200px; height: 849px; }

  .label {
    position: absolute; top: 262px; width: 183px; height: 524px;
    border-radius: 6px; overflow: hidden; color: #fff;
    font-family: "Oswald", "Arial Narrow", sans-serif;
  }
  .label--wheel  { left: 37px;  background: linear-gradient(90deg, var(--blue-a), var(--blue-b) 45%, var(--blue-c) 68%, var(--blue-b)); }
  .label--tire   { left: 264px; background: linear-gradient(90deg, var(--pink-a), var(--pink-b) 45%, var(--pink-c) 68%, var(--pink-b)); }
  .label--apc    { left: 494px; background: linear-gradient(90deg, var(--lime-a), var(--lime-b) 45%, var(--lime-c) 68%, var(--lime-b)); }
  .label--glass  { left: 714px; background: linear-gradient(90deg, var(--orange-a), var(--orange-b) 45%, var(--orange-c) 68%, var(--orange-b)); }

  .monogram {
    position: absolute; left: 36px; top: 40px; width: 111px; height: 227px;
    background: linear-gradient(135deg, var(--silver-light), var(--silver-dark) 60%, var(--silver-light));
    opacity: .85;
  }
  .product-name {
    position: absolute; left: 0; right: 0; top: 282px; text-align: center;
    font-weight: 700; font-size: 21px; line-height: 24px; letter-spacing: .3px;
    color: var(--silver-light);
  }
  .product-claim {
    position: absolute; left: 0; right: 0; top: 337px; text-align: center;
    font-weight: 600; font-size: 8.5px; line-height: 12.5px; color: var(--silver-light);
  }
  .brand-band {
    position: absolute; left: 0; right: 0; top: 372px; height: 62px;
    background: linear-gradient(90deg, var(--silver-dark), var(--silver-light) 40%, var(--silver-mid));
    display: flex; align-items: center; justify-content: center;
    font-family: "Montserrat", sans-serif; font-weight: 600; font-size: 30px; letter-spacing: -.5px;
  }
  .label--wheel .brand-band { color: var(--blue-brand); }
  .label--tire  .brand-band { color: var(--pink-brand); }
  .label--apc   .brand-band { color: var(--lime-brand); }
  .label--glass .brand-band { color: var(--orange-brand); }

  .origin { position: absolute; left: 22px; top: 446px; width: 56px; text-align: center; color: var(--silver-light); }
  .origin-mark { display: block; margin: 0 auto 8px; width: 22px; height: 22px; background: var(--silver-light); }
  .origin-text { font-weight: 600; font-size: 10px; line-height: 14px; }
  .eco-seal { position: absolute; right: 18px; top: 448px; width: 52px; height: 52px; border-radius: 50%;
    border: 2px solid var(--silver-light); background: rgba(255,255,255,.35); }

  .print-master {
    position: absolute; left: 917px; top: 73px; width: 259px; height: 711px;
    border: 1px solid var(--ink); background: #fff; color: var(--ink);
    font-family: "Oswald", "Arial Narrow", sans-serif;
  }
  .print-master .monogram { left: 51px; top: 22px; width: 158px; height: 330px; background: var(--ink); opacity: 1; }
  .print-master .product-name { top: 376px; font-size: 33px; line-height: 36px; color: var(--ink); }
  .print-master .product-claim { top: 456px; font-size: 12px; line-height: 18px; color: var(--ink); }
  .print-master .brand-band { top: 506px; height: 92px; background: var(--ink); color: #fff; font-size: 48px; }
  .print-master .origin { left: 32px; top: 612px; width: 78px; color: var(--ink); }
  .print-master .origin-mark { width: 32px; height: 32px; margin-bottom: 12px; background: var(--ink); }
  .print-master .origin-text { font-size: 16px; line-height: 20px; }
  .print-master .eco-seal { right: 38px; top: 620px; width: 76px; height: 76px; border: 3px solid var(--ink); background: var(--ink); }
</style>
</head>
<body>
<main class="sheet">
  <section class="label label--wheel">
    <div class="monogram" role="img" aria-label="Large silver lettered monogram for Wheel Cleaner"></div>
    <h2 class="product-name">WHEEL<br>CLEANER</h2>
    <p class="product-claim">EFFECTIVE ACID-FREE &amp;<br>PH NEUTRAL WHEEL CLEANER.</p>
    <div class="brand-band">varnity</div>
    <div class="origin"><span class="origin-mark" role="img" aria-label="Origin badge"></span><p class="origin-text">PURE: EST<br>SWEDEN</p></div>
    <div class="eco-seal" role="img" aria-label="Eco-friendly seal"></div>
  </section>

  <section class="label label--tire">
    <div class="monogram" role="img" aria-label="Large silver lettered monogram for Tire Shine"></div>
    <h2 class="product-name">TIRE<br>SHINE</h2>
    <p class="product-claim">HIGHLY EFFECTIVE &amp;<br>LONG LASTING TIRE SHINE.</p>
    <div class="brand-band">varnity</div>
    <div class="origin"><span class="origin-mark" role="img" aria-label="Origin badge"></span><p class="origin-text">PURE: EST<br>SWEDEN</p></div>
    <div class="eco-seal" role="img" aria-label="Eco-friendly seal"></div>
  </section>

  <section class="label label--apc">
    <div class="monogram" role="img" aria-label="Large silver lettered monogram for All Purpose Cleaner"></div>
    <h2 class="product-name">ALL PURPOSE<br>CLEANER</h2>
    <p class="product-claim">PERFECT FOR<br>INTERIOR CLEANING..</p>
    <div class="brand-band">varnity</div>
    <div class="origin"><span class="origin-mark" role="img" aria-label="Origin badge"></span><p class="origin-text">PURE: EST<br>SWEDEN</p></div>
    <div class="eco-seal" role="img" aria-label="Eco-friendly seal"></div>
  </section>

  <section class="label label--glass">
    <div class="monogram" role="img" aria-label="Large silver lettered monogram for Glass Cleaner"></div>
    <h2 class="product-name">GLASS<br>CLEANER</h2>
    <p class="product-claim">PERFECT FOR<br>WINDOW CLEANING..</p>
    <div class="brand-band">varnity</div>
    <div class="origin"><span class="origin-mark" role="img" aria-label="Origin badge"></span><p class="origin-text">PURE: EST<br>SWEDEN</p></div>
    <div class="eco-seal" role="img" aria-label="Eco-friendly seal"></div>
  </section>

  <section class="print-master">
    <div class="monogram" role="img" aria-label="Large black lettered monogram for Wheel Cleaner"></div>
    <h2 class="product-name">WHEEL<br>CLEANER</h2>
    <p class="product-claim">EFFECTIVE ACID-FREE &amp;<br>PH NEUTRAL WHEEL CLEANER.</p>
    <div class="brand-band">varnity</div>
    <div class="origin"><span class="origin-mark" role="img" aria-label="Origin badge"></span><p class="origin-text">PURE: EST<br>SWEDEN</p></div>
    <div class="eco-seal" role="img" aria-label="Eco-friendly seal"></div>
  </section>
</main>
</body>
</html>
```